Keep Tomorrow Book Cover

I am looking for book front cover ideas. The book trim size will be 5.5 x 8.5 in so please make the mock up that size. The book Title is "Keep Tomorrow" and the Subtitle is "Counsel for the Crossroads Nobody Warns You About". The audience for the book is leaders in high-growth companies. It consists of a series of letters and advice for specific problems the leader will encounter on their journey. The design needs to be attractive to both male and female readers. I am attaching a file with brand colors and some rough ideas that need to be refined. The examples lean toward a feminine vibe but I want the cover to be more universal. Please use the brand colors identified in the file.

```html
<!DOCTYPE html>
<html lang="en">
<head>
<meta charset="utf-8">
<title>Keep Tomorrow — Book Cover</title>
<link href="https://fonts.googleapis.com/css2?family=Libre+Caslon+Text:wght@400;700&family=Roboto:wght@400;500&display=swap" rel="stylesheet">
<style>
  :root {
    --stage: #e4e4e2;
    --sage: #b1bea9;
    --ink: #151515;
    --copper: #c8925c;
    --cream: #f2e9d4;
    --tan: #cc9e68;
    --leaf-dark: #3a3f44;
    --leaf-green: #7f9a78;
  }
  * { margin: 0; padding: 0; box-sizing: border-box; }
  html, body {
    width: 1200px;
    height: 730px;
    overflow: hidden;
    background: var(--stage);
  }
  .stage {
    width: 1200px;
    height: 730px;
    display: flex;
    align-items: center;
    justify-content: center;
  }
  .cover {
    width: 440px;
    height: 680px;
    background: var(--sage);
    display: flex;
    flex-direction: column;
    align-items: center;
    padding: 46px 32px 0;
    box-shadow: 0 6px 18px rgba(0,0,0,0.15);
  }
  .cover__title {
    font-family: "Libre Caslon Text", Georgia, serif;
    font-weight: 400;
    font-size: 43px;
    line-height: 1;
    letter-spacing: -0.5px;
    color: var(--ink);
    text-transform: uppercase;
    text-align: center;
    white-space: nowrap;
  }
  .cover__subtitle {
    margin-top: 12px;
    font-family: "Roboto", Arial, sans-serif;
    font-weight: 500;
    font-size: 13.5px;
    line-height: 1.2;
    letter-spacing: 0.4px;
    color: var(--copper);
    text-transform: uppercase;
    text-align: center;
    max-width: 300px;
  }
  .cover__art {
    margin-top: 24px;
    width: 330px;
    height: 400px;
  }
  .cover__author {
    margin-top: 46px;
    font-family: "Roboto", Arial, sans-serif;
    font-weight: 400;
    font-size: 21px;
    letter-spacing: 1px;
    color: var(--cream);
    text-transform: uppercase;
    text-align: center;
  }
</style>
</head>
<body>
  <main class="stage">
    <article class="cover">
      <h1 class="cover__title">Keep Tomorrow</h1>
      <p class="cover__subtitle">Counsel for the Crossroads Nobody Warns You About</p>
      <svg class="cover__art" viewBox="0 0 330 400" role="img" aria-label="Illustration of a leafy tree growing out of an open envelope in dark, green and tan tones">
        <defs>
          <linearGradient id="artTone" x1="0" y1="0" x2="0" y2="1">
            <stop offset="0" stop-color="var(--leaf-green)"/>
            <stop offset="0.45" stop-color="var(--leaf-dark)" stop-opacity="0.55"/>
            <stop offset="0.6" stop-color="var(--tan)"/>
            <stop offset="1" stop-color="var(--cream)"/>
          </linearGradient>
        </defs>
        <rect x="0" y="0" width="330" height="400" rx="12" fill="url(#artTone)"/>
      </svg>
      <p class="cover__author">Marguerite Ellison Hale</p>
    </article>
  </main>
</body>
</html>
```